Leaflets
We supply stone and solid surfaces to the trade and project manage its installation
Project: Leaflets
Leaflets - Construction
Creative Brief
Construction
Architects, Interior designers, property developers, kitchen and bathroom designers, shopfitters Our offer is mainly business to business. Our branding and images are corporate and our content (wording) is more casual (which is what makes us different from the competition)
A leaflet with our branding, logos and fonts to be used as an introduction to our clients mainly targeted trough site visits and by posting samples. Images and branding available on request.

```html
<!DOCTYPE html>
<html lang="en">
<head>
<meta charset="utf-8">
<title>Trelvax Surfaces Leaflet</title>
<link rel="stylesheet" href="https://fonts.googleapis.com/css2?family=Arimo:wght@400;700&display=swap">
<style>
  :root {
    --green: #8cc63f;
    --purple: #7b2a8f;
    --grey-box: #9a9a9a;
    --grey-text: #b5b5b5;
    --white: #ffffff;
    --paper: #ffffff;
  }
  * { margin: 0; padding: 0; box-sizing: border-box; }
  html, body { width: 1200px; height: 932px; overflow: hidden; background: var(--paper); }
  .leaflet {
    position: relative; width: 1200px; height: 932px; overflow: hidden;
    font-family: "Arimo", Arial, sans-serif; background: var(--paper);
  }
  .block { position: absolute; }
  .photo-bathroom {
    left: 0; top: 0; width: 392px; height: 265px;
    background: linear-gradient(160deg, #f4f6f6 0%, #dfe6e8 45%, #1fa9c9 62%, #2b6f7c 80%, #e9eded 100%);
  }
  .photo-worktop {
    left: 400px; top: 0; width: 800px; height: 265px;
    background: linear-gradient(180deg, #c9d3c2 0%, #eef0ec 40%, #d9d6d0 70%, #f3f2ef 100%);
  }
  .band { background: var(--purple); }
  .band-top { left: 400px; top: 278px; width: 800px; height: 20px; }
  .band-bottom { left: 400px; top: 540px; width: 800px; height: 18px; }
  .intro-panel {
    left: 0; top: 295px; width: 400px; height: 240px; background: var(--green);
    color: var(--white); font-size: 12.6px; line-height: 1.3; padding: 26px 26px 0 55px;
    text-align: justify;
  }
  .address-box {
    left: 424px; top: 323px; width: 258px; height: 77px; background: var(--grey-box);
    color: var(--white); font-size: 21px; line-height: 1.25; padding: 8px 12px; font-style: normal;
  }
  .contact {
    left: 432px; top: 420px; color: var(--purple); font-size: 14.5px; line-height: 27px;
  }
  .brand {
    left: 860px; top: 388px; color: var(--purple); font-weight: 700;
    font-size: 38px; line-height: 1; white-space: nowrap;
  }
  .story {
    left: 55px; top: 598px; width: 320px; color: var(--grey-text);
    font-size: 13.2px; line-height: 1.36; text-align: justify;
  }
  .photo-kitchen {
    left: 400px; top: 558px; width: 800px; height: 374px;
    background: linear-gradient(180deg, #8b9a7f 0%, #c7c9bd 30%, #7e6f60 55%, #5b4c3f 75%, #a39a8e 100%);
  }
  .offer-box {
    left: 803px; top: 662px; width: 397px; height: 96px; background: var(--green);
    color: var(--white); font-size: 17px; line-height: 1.3; text-align: right; padding: 20px 22px 0 70px;
  }
  .web-tab {
    left: 922px; top: 861px; width: 278px; height: 59px; background: var(--purple);
    color: var(--white); font-size: 18px; display: flex; align-items: center; justify-content: center;
  }
</style>
</head>
<body>
<main class="leaflet">
  <div class="block photo-bathroom" role="img" aria-label="Bathroom with white basins on a turquoise solid surface vanity"></div>
  <div class="block photo-worktop" role="img" aria-label="Bright room with white stone worktop, basins and chairs"></div>

  <div class="block band band-top"></div>

  <section class="block intro-panel">
    <p>Please go to our Gallery to view our recently completed work. If you like what you see and want to get to know us better, our Blog is a scrapbook of commercial and residential projects, ideas, designs, and things we just want to share with the wider world.</p>
  </section>

  <address class="block address-box">88 Harrow Lane<br>London, E9 2QT</address>

  <div class="block contact">
    <div>02079460318</div>
    <div>07700900412</div>
    <div>mail@trelvaxsurfaces.co.uk</div>
    <div>www.trelvaxsurfaces.co.uk</div>
  </div>

  <div class="block brand">Trelvax Surfaces</div>

  <div class="block band band-bottom"></div>

  <section class="block story">
    <p>We share ten years' experience working in the stone industry; we know how time-consuming sourcing high quality products can be, not to mention the leg work that goes into finding experienced project managers and expert craftspeople to carry out the work. So what we've come up with is a complete service: you tell us what you need, we source the stone, put together the team, oversee the job and follow up with you afterwards to make sure everything is perfect. It sounds easy and straight-forward – and it is, but very few companies offer such a comprehensive package.</p>
  </section>

  <div class="block photo-kitchen" role="img" aria-label="Kitchen with brown stone worktop and stacked white plates"></div>

  <div class="block offer-box">We supply stone and solid surfaces to the trade and project manage its installation</div>

  <div class="block web-tab">www.trelvaxsurfaces.co.uk</div>
</main>
</body>
</html>
```